Stationary Set Rebrand for Brenvik

We are a Canadian Distribution and Service Company that was established in 1969. Over the past 5 decades we have expanded our business and have warehouses across Canada. We specialize in adhesive tapes, adhesives, films, safety, warehouse, shipping, janitorial and packaging supplies.

We have updated our logo design and would like a new corporate branding identity that includes a new fresh Stationary Set (Business Cards, Letterhead, Letterhead MS Word, Envelope, Presentation Folders, Email Signatures, Notepad Covers, etc.)

Target Market(s)

Industrial Business Sector

Font styles to use
Sans Serif

Colors
0054AA
0677BA
7BADD7
CADEEF
E8F1F8
0094D4
00A9DD
6FCCEA
C7EBF8
E9F6FB
00AB8E
00BBA5
67D7C9
C6EFE9
E9F9F6
EB3D1F
EC4F4E
F09395
F8D3D4
FCEDEE

Requirements
Should not have
• Colors not too light, darker colours preferred

```html
<!DOCTYPE html>
<html lang="en">
<head>
<meta charset="utf-8">
<title>Brenvik Business Card</title>
<link rel="stylesheet" href="https://fonts.googleapis.com/css2?family=Saira:wght@400;500;700;800&family=Michroma&display=swap">
<style>
  :root {
    --bg: #e4e4e4;
    --card-white: #ffffff;
    --ink: #231f20;
    --text-grey: #4a4a4a;
    --muted-grey: #6b6b6b;
    --rule: #b5b5b5;
    --brand-red: #d7191f;
    --back-dark: #1c1c1d;
    --back-mid: #2c2c2e;
    --back-light: #3a3a3c;
  }
  * { margin: 0; padding: 0; box-sizing: border-box; }
  html, body {
    width: 1200px; height: 1200px; overflow: hidden;
    background: var(--bg);
    font-family: "Saira", sans-serif;
  }
  .canvas { position: relative; width: 1200px; height: 1200px; }

  .card {
    position: absolute; left: 260px; width: 696px; height: 398px;
    box-shadow: 0 14px 28px rgba(0,0,0,0.28);
    overflow: hidden;
  }
  .card-front { top: 156px; background: var(--card-white); }
  .card-back { top: 651px; }

  .brand-name {
    position: absolute; right: 50px; top: 34px;
    font-family: "Saira", sans-serif; font-weight: 800;
    font-size: 68px; line-height: 1; color: var(--ink);
    letter-spacing: -1px;
  }

  .person-name {
    position: absolute; left: 48px; top: 228px;
    font-family: "Michroma", sans-serif; font-size: 23px; line-height: 1;
    color: var(--brand-red); letter-spacing: 0.5px;
  }
  .person-title {
    position: absolute; left: 49px; top: 254px;
    font-size: 15px; color: var(--muted-grey); letter-spacing: 0.6px;
  }
  .divider {
    position: absolute; left: 49px; right: 43px; top: 284px;
    height: 1px; background: var(--rule);
  }

  .contact-list { position: absolute; left: 44px; top: 292px; list-style: none; }
  .contact-item {
    display: flex; align-items: center; height: 21px;
    font-size: 17px; color: var(--text-grey); letter-spacing: 0.6px;
  }
  .contact-icon { width: 16px; height: 16px; margin-right: 11px; fill: var(--brand-red); }

  .address {
    position: absolute; right: 41px; top: 294px; text-align: right;
    font-size: 17px; line-height: 21px; color: var(--text-grey); letter-spacing: 0.6px;
    font-style: normal;
  }

  .footer-band {
    position: absolute; left: 0; bottom: 0; width: 100%; height: 16px; background: var(--ink);
  }
  .footer-tab { position: absolute; right: 0; bottom: 0; width: 290px; height: 33px; }
  .web-address {
    position: absolute; right: 41px; bottom: 6px;
    font-size: 17px; font-weight: 500; color: #ffffff; letter-spacing: 0.6px;
  }

  .back-pattern {
    width: 100%; height: 100%;
    background: linear-gradient(90deg, var(--back-dark) 0%, var(--back-mid) 45%, var(--back-light) 100%);
  }
</style>
</head>
<body>
<div class="canvas">

  <section class="card card-front">
    <div class="brand-name">Brenvik</div>

    <h1 class="person-name">DANIEL HARPER</h1>
    <p class="person-title">President</p>
    <div class="divider"></div>

    <ul class="contact-list">
      <li class="contact-item">
        <svg class="contact-icon" viewBox="0 0 24 24"><path d="M6.6 10.8c1.4 2.8 3.8 5.1 6.6 6.6l2.2-2.2c.3-.3.7-.4 1-.2 1.1.4 2.3.6 3.6.6.6 0 1 .4 1 1V20c0 .6-.4 1-1 1C10.6 21 3 13.4 3 4c0-.6.4-1 1-1h3.5c.6 0 1 .4 1 1 0 1.3.2 2.5.6 3.6.1.3 0 .7-.2 1L6.6 10.8z"/></svg>
        604-218-5390
      </li>
      <li class="contact-item">
        <svg class="contact-icon" viewBox="0 0 24 24"><path d="M7 1h10a2 2 0 0 1 2 2v18a2 2 0 0 1-2 2H7a2 2 0 0 1-2-2V3a2 2 0 0 1 2-2zm0 3v14h10V4H7zm5 15.2a1.1 1.1 0 1 0 0 2.2 1.1 1.1 0 0 0 0-2.2z"/></svg>
        604-771-4826
      </li>
      <li class="contact-item">
        <svg class="contact-icon" viewBox="0 0 24 24"><path d="M2 5h20v14H2V5zm2 2v.4l8 5.2 8-5.2V7H4zm0 2.8V17h16V9.8l-8 5.2-8-5.2z"/></svg>
        info@brenvik.com
      </li>
    </ul>

    <address class="address">
      2145 Harbourview Road<br>
      Kelowna, Canada V1Y 2K8
    </address>

    <div class="footer-band"></div>
    <svg class="footer-tab" viewBox="0 0 290 33" preserveAspectRatio="none">
      <polygon points="0,33 6,27 290,27 290,33" fill="#ffffff"/>
      <polygon points="4,33 32,0 290,0 290,33" fill="var(--brand-red)"/>
    </svg>
    <span class="web-address">www.brenvik.com</span>
  </section>

  <section class="card card-back">
    <div class="back-pattern" role="img" aria-label="Repeating leaf pattern in graded dark greys with one red accent leaf near the lower right"></div>
  </section>

</div>
</body>
</html>
```